Web Design Project - Event Management Company

A web-page design needs to be created for an event management company. The logo has already been created, the design needs to draw on the themes and colors of the logo and extend on that.

The event management company likes to differentiate itself from others by being a bit "un-conventional" and being able to think outside the box.

the specialise in corporate events, weddings, AGMs, anything that requires coordination of resources. They also can provide Audio Visual services such as recording events.

final design will also require HTML implementation

```html
<!DOCTYPE html>
<html lang="en">
<head>
<meta charset="utf-8">
<title>Odd Block Collective</title>
<link rel="stylesheet" href="https://fonts.googleapis.com/css2?family=Carlito:wght@400;700&family=Open+Sans:wght@400;600;700&display=swap">
<style>
:root{
  --nav-bg:#2b2b2b;
  --nav-text:#e4e4e4;
  --accent:#29b6f0;
  --link-blue:#2aa6e0;
  --ink:#1e1e1e;
  --body:#555;
  --muted:#6b6b6b;
  --rule:#dcdcdc;
  --arrow:#f07a3a;
  --logo:#4a4a4a;
  --panel:#ffffff;
  --footer:rgba(215,215,215,.88);
}
*{margin:0;padding:0;box-sizing:border-box}
html,body{width:1200px;height:981px;overflow:hidden}
body{position:relative;font-family:"Open Sans",Arial,sans-serif;color:var(--body);background:#d9d3c9}
.backdrop{position:absolute;inset:0;background:
  radial-gradient(ellipse 45% 30% at 50% 18%,rgba(255,255,255,.75) 0%,rgba(255,255,255,0) 100%),
  radial-gradient(ellipse 30% 25% at 10% 55%,rgba(214,205,170,.55) 0%,rgba(214,205,170,0) 100%),
  radial-gradient(ellipse 30% 25% at 92% 55%,rgba(200,190,165,.55) 0%,rgba(200,190,165,0) 100%),
  linear-gradient(180deg,#e9e8e3 0%,#dcdad2 30%,#d4ccbd 55%,#c9bba7 78%,#bfae98 100%)}
.nav{position:absolute;left:0;top:0;width:1200px;height:36px;background:var(--nav-bg)}
.nav a{position:absolute;top:0;height:36px;line-height:36px;font-size:15.5px;color:var(--nav-text);text-decoration:none}
.nav a.current{background:var(--accent);color:#fff;padding:0 13px}
.nav-tab{position:absolute;left:579px;top:36px;width:36px;height:23px;background:var(--accent)}
.brand{position:absolute;left:0;top:64px;width:1200px;text-align:center;font-family:"Carlito",sans-serif;font-size:38px;color:var(--logo);letter-spacing:1px}
.brand-mark{position:absolute;left:580px;top:120px;width:34px;height:34px;background:#f59a2a}
.panel{position:absolute;left:165px;top:319px;width:864px;height:481px;background:var(--panel);border-radius:16px;box-shadow:0 0 6px rgba(0,0,0,.15)}
.close{position:absolute;left:826px;top:20px}
.intro-title{position:absolute;left:47px;top:38px;font-family:"Carlito",sans-serif;font-size:33px;font-weight:400;color:var(--ink);white-space:nowrap}
.intro-text{position:absolute;left:50px;top:91px;width:450px;font-size:13px;line-height:19.7px}
.feature{position:absolute;left:50px;width:450px}
.feature-photo{position:absolute;left:0;top:0;width:163px;height:118px;border:1px solid #d6d6d6;border-radius:7px;padding:3px;background:#fff}
.feature-photo span{display:block;width:100%;height:100%;border-radius:5px}
.feature h3{position:absolute;left:182px;top:2px;font-size:13.5px;font-weight:600;color:var(--link-blue)}
.feature p{position:absolute;left:182px;top:28px;width:270px;font-size:11px;line-height:16.3px;color:var(--muted)}
.read-more{position:absolute;left:182px;top:104px;font-size:11.5px;color:#444;padding-left:14px}
.read-more::before{content:"";position:absolute;left:0;top:5px;border:3.5px solid transparent;border-left:5px solid var(--arrow)}
.divider{position:absolute;left:522px;top:47px;width:1px;height:401px;background:var(--rule)}
.news-title{position:absolute;left:554px;top:46px;font-family:"Carlito",sans-serif;font-size:33px;font-weight:400;color:var(--ink)}
.news-list{position:absolute;left:554px;top:92px;width:237px;height:352px;overflow:hidden}
.news-item{padding-bottom:14px;margin-bottom:12px;border-bottom:1px solid var(--rule)}
.news-item time{display:block;font-size:13px;color:var(--link-blue);margin-bottom:7px}
.news-item p{font-size:11px;line-height:16.3px;color:var(--muted)}
.news-item a{color:#999}
.scrollbar{position:absolute;left:801px;top:92px;width:12px;height:352px;border:1px solid #e2e2e2;border-radius:6px}
.scroll-thumb{position:absolute;left:2px;top:20px;width:6px;height:60px;background:var(--accent);border-radius:3px}
.footer{position:absolute;left:0;top:945px;width:1200px;height:36px;background:var(--footer)}
.copyright{position:absolute;left:30px;top:11px;font-size:11px;color:#555}
.copyright a{color:#777}
.social{position:absolute;right:26px;top:10px;display:flex;gap:14px}
.social a{font-size:11px;font-weight:600;color:#fff;text-decoration:none;white-space:nowrap}
</style>
</head>
<body>
<div class="backdrop" role="img" aria-label="Photo of an elegant marquee dining room with draped white ceiling, chandeliers and set banquet tables"></div>

<nav class="nav">
  <a class="current" href="#" style="left:286px">Home page</a>
  <a href="#" style="left:405px">About us</a>
  <a href="#" style="left:493px">Services</a>
  <a href="#" style="left:587px">Events</a>
  <a href="#" style="left:666px">Gallery</a>
  <a href="#" style="left:755px">Video</a>
  <a href="#" style="left:836px">Contacts</a>
</nav>
<div class="nav-tab"><svg width="36" height="23"><path d="M11 15 L18 8 L25 15 M11 19 L18 12 L25 19" fill="none" stroke="#fff" stroke-width="1.4"/></svg></div>

<div class="brand">ODD BLOCK COLLECTIVE</div>
<div class="brand-mark"></div>

<main class="panel">
  <svg class="close" width="16" height="16"><path d="M2 2 L14 14 M14 2 L2 14" stroke="#999" stroke-width="3"/></svg>
  <h1 class="intro-title">Welcome to Odd Block Collective</h1>
  <p class="intro-text">Lorem ipsum dolor sit amet conse ctetur adipisicing elit, sed do eiusmod tempor incididunt ut labore et dolore magna. Ipsum dolor sit amet conse ctetur adipisicing elit, sed do eiusmod tempor.</p>

  <section class="feature" style="top:157px">
    <div class="feature-photo"><span role="img" aria-label="Photo of a boardroom table with red leather chairs" style="background:linear-gradient(135deg,#d9d2cc,#8c2a2e 55%,#3a2220)"></span></div>
    <h3>Who We Are</h3>
    <p>Lorem ipsum dolor sit amet conse ctetur adipisicing elit, sed do eiusmod tempor incididunt ut labore et dolore magna. Ipsum dolor sit amet conse ctetur adipisicing elit, sed do eiusmod tempor.</p>
    <span class="read-more">READ MORE</span>
  </section>

  <section class="feature" style="top:310px">
    <div class="feature-photo">
      <span role="img" aria-label="Video still of a business team standing in an office" style="background:linear-gradient(180deg,#e6e8ea,#9a9ea4 60%,#3c3f44);position:relative">
        <svg width="80" height="52" style="position:absolute;left:43px;top:31px"><rect x="1" y="1" width="78" height="50" rx="10" fill="#2a2a2a" stroke="#111"/><path d="M31 13 L53 26 L31 39 Z" fill="#fff"/></svg>
      </span>
    </div>
    <h3>Video Presentation</h3>
    <p>Lorem ipsum dolor sit amet conse ctetur adipisicing elit, sed do eiusmod tempor incididunt ut labore et dolore magna. Ipsum dolor sit amet conse ctetur adipisicing elit, sed do eiusmod tempor.</p>
    <span class="read-more">READ MORE</span>
  </section>

  <div class="divider"></div>

  <h2 class="news-title">Latest News</h2>
  <div class="news-list">
    <article class="news-item">
      <time>18 of March 2013</time>
      <p>Lorem ipsum dolor sit amet conse ctetur adipisicing elit, sed do eiusmod tempor incididunt ut labore et dolore magna. Ipsum dolor sit amet conse ctetur adipisicing elit, sed do eiusmod tempor.</p>
    </article>
    <article class="news-item">
      <time>22 of April 2013</time>
      <p>Incididunt ut labore et dolore magna aliqua. Ut enim ad minim veniam, quis nostrud exercitation ullamco laboris nisi ut aliquip ex ea commodo consequat consectetuer adipiscing elit. Nunc suscipit. <a href="#">read more</a></p>
    </article>
    <article class="news-item">
      <time>05 of May 2013</time>
      <p>Lorem ipsum dolor sit amet conse ctetur adipisicing elit, sed do eiusmod tempor incididunt ut labore et dolore magna. Ipsum dolor sit amet conse ctetur adipisicing elit, sed do eiusmod tempor.</p>
    </article>
  </div>
  <div class="scrollbar"><div class="scroll-thumb"></div></div>
</main>

<footer class="footer">
  <p class="copyright">Copyright © 2013. All rights reserved. &nbsp;/ &nbsp;<a href="#">Privacy Policy</a></p>
  <nav class="social">
    <a href="#">Chirp</a>
    <a href="#">Facefeed</a>
    <a href="#">Linkwork</a>
  </nav>
</footer>
</body>
</html>
```